Marta Business Card

My wife is going to start her own business with renting holiday appartments to tourists. She needs a design for a new business card... and a new web site.
Look at Stayvolt "Erholung auf dem Lindenwäldchen"

Target Market(s)

Give business card to prospects at any situation

Contact Information for Business Card

not sure what this means

Font styles to use
Script

Colors
fec41a
fee18a

Requirements
Must have
• My wife's handwriting is difficult to read:
Entspannen - Loslassen - Auftanken
Marta & das Lindenwäldchen
Urlaub an einem besonderen Ort
Marta Brecke
Grauer Pfad 7
18471 Alt Feldow
post@marta-brecke.de
www.lindenwaeldchen.net
Nice to have
• Beige background
Font like handwriting

```html
<!DOCTYPE html>
<html lang="de">
<head>
<meta charset="utf-8">
<title>Marta Brecke – Visitenkarte</title>
<link rel="stylesheet" href="https://fonts.googleapis.com/css2?family=Damion&family=Jost:wght@300;400&display=block">
<style>
  :root {
    --page-bg: #eed9da;
    --card-bg: #8f7867;
    --card-bg-light: #978070;
    --gold: #fec41a;
    --gold-soft: #fee18a;
  }
  * { box-sizing: border-box; margin: 0; padding: 0; }
  html, body {
    width: 1200px;
    height: 1170px;
    overflow: hidden;
    background: var(--page-bg);
  }
  .canvas {
    width: 1200px;
    height: 1170px;
    display: flex;
    flex-direction: column;
    align-items: center;
    justify-content: center;
    gap: 64px;
  }
  .card {
    width: 760px;
    height: 440px;
    background: linear-gradient(135deg, var(--card-bg-light), var(--card-bg));
    box-shadow: 0 14px 34px rgba(80, 55, 45, 0.18);
    color: var(--gold);
  }

  /* Front side */
  .card-front {
    display: flex;
    align-items: center;
    justify-content: center;
    padding: 0 50px;
  }
  .holder-name {
    font-family: "Damion", "Brush Script MT", cursive;
    font-size: 60px;
    font-weight: 400;
    letter-spacing: 1px;
    white-space: nowrap;
    flex: none;
    transform: translateY(14px);
  }
  .divider {
    flex: none;
    width: 1.5px;
    height: 170px;
    background: var(--gold);
    opacity: 0.85;
    margin: 0 36px 0 36px;
  }
  .contact-list {
    flex: none;
    list-style: none;
    font-family: "Jost", sans-serif;
    font-weight: 300;
    font-size: 17px;
    line-height: 1.3;
    transform: translateY(-14px);
  }
  .contact-list li {
    display: flex;
    align-items: flex-start;
    gap: 12px;
    margin-bottom: 12px;
    white-space: nowrap;
  }
  .contact-list li:last-child { margin-bottom: 0; }
  .contact-icon {
    width: 14px;
    height: 14px;
    flex: none;
    margin-top: 3px;
    fill: var(--gold);
  }

  /* Back side */
  .card-back {
    display: flex;
    flex-direction: column;
    align-items: center;
    justify-content: center;
    font-family: "Damion", "Brush Script MT", cursive;
    font-size: 40px;
    line-height: 1.35;
    text-align: center;
  }
</style>
</head>
<body>
<main class="canvas">
  <section class="card card-front" aria-label="Visitenkarte Vorderseite">
    <h1 class="holder-name">Marta Brecke</h1>
    <div class="divider"></div>
    <ul class="contact-list">
      <li>
        <svg class="contact-icon" viewBox="0 0 24 24" aria-hidden="true"><path d="M6.6 10.8a15.1 15.1 0 0 0 6.6 6.6l2.2-2.2a1 1 0 0 1 1-.25 11.4 11.4 0 0 0 3.6.57 1 1 0 0 1 1 1V20a1 1 0 0 1-1 1A17 17 0 0 1 3 4a1 1 0 0 1 1-1h3.5a1 1 0 0 1 1 1c0 1.25.2 2.450.57 3.57a1 1 0 0 1-.25 1z"/></svg>
        <span>+49 152 480 316 54</span>
      </li>
      <li>
        <svg class="contact-icon" viewBox="0 0 24 24" aria-hidden="true"><path d="M12 2a10 10 0 1 0 5 18.7l-1-1.7A8 8 0 1 1 20 12v1.5a1.5 1.5 0 0 1-3 0V7h-2v1a5 5 0 1 0 .6 7.5A3.5 3.5 0 0 0 22 13.5V12A10 10 0 0 0 12 2zm0 13a3 3 0 1 1 0-6 3 3 0 0 1 0 6z"/></svg>
        <span>post@marta-brecke.de</span>
      </li>
      <li>
        <svg class="contact-icon" viewBox="0 0 24 24" aria-hidden="true"><path d="M12 2a10 10 0 1 0 0 20 10 10 0 0 0 0-20zm6.9 6h-2.9a15 15 0 0 0-1.4-3.6A8 8 0 0 1 18.9 8zM12 4a13 13 0 0 1 1.9 4h-3.8A13 13 0 0 1 12 4zM4.3 14a8 8 0 0 1 0-4h3.4a16 16 0 0 0 0 4zm.8 2h2.9a15 15 0 0 0 1.4 3.6A8 8 0 0 1 5.1 16zM8 8H5.1a8 8 0 0 1 4.3-3.6A15 15 0 0 0 8 8zm4 12a13 13 0 0 1-1.9-4h3.8A13 13 0 0 1 12 20zm2.3-6H9.7a14 14 0 0 1 0-4h4.6a14 14 0 0 1 0 4zm.3 5.6A15 15 0 0 0 16 16h2.9a8 8 0 0 1-4.3 3.6zm1.7-5.6a16 16 0 0 0 0-4h3.4a8 8 0 0 1 0 4z"/></svg>
        <span>www.lindenwaeldchen.net</span>
      </li>
      <li>
        <svg class="contact-icon" viewBox="0 0 24 24" aria-hidden="true"><path d="M12 2a7 7 0 0 0-7 7c0 5.2 7 13 7 13s7-7.8 7-13a7 7 0 0 0-7-7zm0 9.5a2.5 2.5 0 1 1 0-5 2.5 2.5 0 0 1 0 5z"/></svg>
        <span>Grauer Pfad 7, 18471<br>Alt Feldow, Germany</span>
      </li>
    </ul>
  </section>

  <section class="card card-back" aria-label="Visitenkarte Rückseite">
    <p class="tagline">Entspannen - Loslassen - Auftanken</p>
    <p class="tagline">Marta &amp; das Lindenwäldchen</p>
    <p class="tagline">Urlaub an einem besonderen Ort</p>
  </section>
</main>
</body>
</html>
```